LUXURY LABEL DESIGN

We are looking for a LUXURY label designer to help us create luxury labels.

Label Color needs to be black , white , and gold very Luxury feel.

I have attached the actual bottle so you can design the label best for the look, logo, barcodes, along with a document with all details including the size of the label.

You can design ONE for now for us to see your quality of work

Target Market(s)

Women or Men wanting skincare

Industry/Entity Type

Beauty

```html
<!DOCTYPE html>
<html lang="en">
<head>
<meta charset="utf-8">
<title>Aurelle – Gentle Exfoliating Body Polish Label</title>
<link href="https://fonts.googleapis.com/css2?family=Cinzel:wght@400;500&family=Josefin+Sans:wght@400&family=Montserrat:wght@400;600;700&display=swap" rel="stylesheet">
<style>
  :root {
    --frame-white: #ffffff;
    --backdrop-light: #4a4a4a;
    --backdrop-dark: #353535;
    --label-black: #0c0c0c;
    --label-deep: #1a1814;
    --gold: #c9a24e;
    --gold-light: #e6c97a;
    --ink-white: #f2f0ea;
  }
  * { box-sizing: border-box; margin: 0; padding: 0; }
  html, body {
    width: 701px; height: 1200px; overflow: hidden;
    background: var(--frame-white);
  }
  .canvas { position: relative; width: 701px; height: 1200px; }

  .stage {
    position: absolute; left: 7px; width: 687px;
    background: radial-gradient(ellipse at 50% 40%, var(--backdrop-light) 0%, var(--backdrop-dark) 100%);
  }
  .stage-front { top: 7px; height: 550px; }
  .stage-second { top: 561px; height: 548px; }

  /* Front face of the label, flat */
  .front-panel {
    position: absolute; left: 50%; top: 50%;
    width: 560px; height: 260px;
    transform: translate(-50%, -50%);
    background: var(--label-black);
    overflow: hidden;
    font-family: "Montserrat", sans-serif;
  }
  .front-texture {
    position: absolute; inset: 0;
    background: radial-gradient(ellipse at 55% 35%, #2a2418 0%, var(--label-deep) 45%, var(--label-black) 100%);
  }
  .front-brand {
    position: absolute; left: 38px; top: 25px; height: 210px; width: 60px;
    writing-mode: vertical-rl; transform: rotate(180deg);
    display: flex; align-items: center; justify-content: center;
    font-family: "Cinzel", serif; font-weight: 500; font-size: 36px;
    letter-spacing: 3px; color: var(--gold); white-space: nowrap;
  }
  .front-title {
    position: absolute; left: 160px; top: 66px; width: 370px; height: 72px;
    border: 1.5px solid var(--gold); background: var(--label-black);
    font-family: "Cinzel", serif; font-weight: 400; color: var(--gold-light);
    font-size: 20px; letter-spacing: 5px; line-height: 1.25;
    text-align: center; padding-top: 9px;
  }
  .front-actives {
    position: absolute; left: 160px; top: 140px; width: 370px; height: 34px;
    border: 1.5px solid var(--gold); background: var(--label-black);
    font-family: "Josefin Sans", sans-serif; font-size: 17px; letter-spacing: 5px;
    text-align: center; line-height: 33px; color: var(--ink-white);
  }
  .front-weight {
    position: absolute; left: 160px; top: 182px; width: 370px;
    display: flex; align-items: center; gap: 6px;
    font-size: 16px; color: var(--ink-white);
  }
  .front-weight .rule { flex: 1; height: 2px; background: var(--gold); margin-top: 10px; }

  /* Full flat label strip */
  .label {
    position: absolute; left: 7px; top: 1113px;
    width: 1445px; height: 160px;
    transform: scale(0.4754); transform-origin: 0 0;
    background: var(--label-black);
    font-family: "Montserrat", sans-serif;
    color: var(--ink-white);
    overflow: hidden;
  }
  .label-texture {
    position: absolute; inset: 0;
    background: radial-gradient(ellipse at 45% 40%, #221e16 0%, var(--label-deep) 45%, var(--label-black) 100%);
  }
  .panel {
    position: absolute; border: 1.5px solid var(--gold);
    background: rgba(8,8,8,0.85);
  }
  .ingredients-panel { left: 98px; top: 12px; width: 390px; height: 136px; }
  .ingredients-text {
    padding: 7px 7px 0; font-size: 10.2px; line-height: 1.2; text-align: justify;
    height: 92px; overflow: hidden;
  }
  .ingredients-text strong, .care-text strong { font-weight: 700; }
  .distributor {
    border-top: 1.5px solid var(--gold); height: 20px;
    font-size: 10px; font-weight: 600; text-align: center; line-height: 19px;
  }
  .origin-row {
    border-top: 1.5px solid var(--gold); display: flex; height: 21px;
    font-size: 10px; font-weight: 600; line-height: 20px;
  }
  .origin-row span { flex: 1; text-align: center; }
  .origin-row span + span { border-left: 1.5px solid var(--gold); }
  .brand-mark {
    position: absolute; left: 550px; top: 12px; width: 60px; height: 136px;
    writing-mode: vertical-rl; transform: rotate(180deg);
    display: flex; align-items: center; justify-content: center;
    font-family: "Cinzel", serif; font-weight: 500; font-size: 24px;
    letter-spacing: 2px; color: var(--gold); white-space: nowrap;
  }
  .product-title {
    position: absolute; left: 652px; top: 40px; width: 252px; height: 46px;
    border: 1.5px solid var(--gold); background: var(--label-black);
    font-family: "Cinzel", serif; color: var(--gold-light);
    font-size: 13px; letter-spacing: 4px; text-align: center; line-height: 1.2;
    padding-top: 6px;
  }
  .product-actives {
    position: absolute; left: 652px; top: 88px; width: 252px; height: 18px;
    border: 1.5px solid var(--gold); background: var(--label-black);
    font-family: "Josefin Sans", sans-serif; font-size: 11px; letter-spacing: 4px;
    text-align: center; line-height: 17px; color: var(--ink-white);
  }
  .net-weight {
    position: absolute; left: 652px; top: 112px; width: 252px;
    display: flex; align-items: center; gap: 4px;
    font-size: 11px; color: var(--ink-white);
  }
  .net-weight .rule { flex: 1; height: 1.5px; background: var(--gold); margin-top: 8px; }
  .care-panel { left: 975px; top: 12px; width: 443px; height: 136px; }
  .care-text {
    font-size: 10.2px; line-height: 1.2; text-align: justify; padding: 7px 9px;
    text-align-last: center;
  }
  .care-text + .care-text { border-top: 1.5px solid var(--gold); }
  .care-text.directions { height: 66px; }
</style>
</head>
<body>
<main class="canvas">
  <section class="stage stage-front" aria-label="Label front face">
    <div class="front-panel">
      <div class="front-texture" role="img" aria-label="Fine gold topographic contour-line pattern on black"></div>
      <div class="front-brand">AURELLE</div>
      <h2 class="front-title">GENTLE EXFOLIATING<br>BODY POLISH</h2>
      <p class="front-actives">TURMERIC + KOJIC ACID</p>
      <p class="front-weight"><span class="rule"></span><span>3.7oz / (100g)</span></p>
    </div>
  </section>

  <section class="stage stage-second" aria-label="Label front face">
    <div class="front-panel">
      <div class="front-texture" role="img" aria-label="Fine gold topographic contour-line pattern on black"></div>
      <div class="front-brand">AURELLE</div>
      <h2 class="front-title">GENTLE EXFOLIATING<br>BODY POLISH</h2>
      <p class="front-actives">TURMERIC + KOJIC ACID</p>
      <p class="front-weight"><span class="rule"></span><span>3.7oz / (100g)</span></p>
    </div>
  </section>

  <section class="label" aria-label="Flat jar label">
    <div class="label-texture" role="img" aria-label="Fine gold topographic contour-line pattern on black"></div>

    <div class="panel ingredients-panel">
      <p class="ingredients-text"><strong>Ingredients:</strong> Glycerin Aqua (Water), Sorbitol, Sodium Lauroyl Isethionate, Disodium Lauryl Sulfosuccinate, Sodium Chloride, Phenoxyethanol, Tetrasodium EDTA,Preservative Caprylyl Glycol, Kojic Acid, Curcuma longa (Turmeric), Zingiber officinale (Ginger), Elaeis guineensis (Palm) Fruit Extract, Persea Gratissima (Avocado) Oil, Simmondsia chinensis (Jojoba) Oil, Sucrose (Organic Cane Sugar) Aurantium Dulcis Sinensis (Orange) Peel Oil, Fragrance Citrus Limonium (Lemon).</p>
      <p class="distributor">Distributed By: Aurelle Beauty Co., LLC Dayton, Tx 77535</p>
      <p class="origin-row"><span>Made In USA</span><span>www.aurellebeautyco.com</span></p>
    </div>

    <div class="brand-mark">AURELLE</div>

    <h1 class="product-title">GENTLE EXFOLIATING<br>BODY POLISH</h1>
    <p class="product-actives">TURMERIC + KOJIC ACID</p>
    <p class="net-weight"><span class="rule"></span><span>3.7oz / (100g)</span></p>

    <div class="panel care-panel">
      <p class="care-text directions"><strong>Directions:</strong> Apply a small amount of Whipped Turmeric Exfoliating Face Scrub with fingertips and gently massage onto damp skin. Spread in small circular motions, can leave on skin for up to three to five minutes, then rinse with warm water. For best results, use 1-2 times a week. Sensitive skin, use once a week.</p>
      <p class="care-text"><strong>Warning:</strong> Not for internal use. Avoid contact with eyes. Do not apply to broken or irritated skin. If sensitivity occurs, discontinue use. Avoid this product if you are allergic or sensitive to any of the ingredients. Keep out of reach of children. Store in a cool, dry place.</p>
    </div>
  </section>
</main>
</body>
</html>
```